Tobin Quartz Portal Page . It's guarantee project!

We need a clean and professional modern web application portal page
That includes the Login & Application Selection screen

Also, I need to design both Desktop and Mobile sizes.
We have an example design for our target

The application is Jetty Schedule and related data.
Our client is a bit conservative.

Theme color preferred : #00508B (main) #DF0D83 (secondary)

Target Market(s)

Oil & Fuel & Gasoline

Number of Pages Required

2 page

Font styles to use
Sans Serif

Colors
0054AA
0677BA
7BADD7
CADEEF
E8F1F8
E54698
E96AAD
F1A4CE
F9D9EA
FCEFF6

Requirements
Must have
• Login Page & Main Screen

```html
<!DOCTYPE html>
<html lang="en">
<head>
<meta charset="utf-8">
<title>Tobin Quartz – Application Selection</title>
<link rel="stylesheet" href="https://fonts.googleapis.com/css2?family=Inter:wght@400;500&family=Poppins:wght@500;600&display=swap">
<style>
:root{
  --blue:#00508B;
  --blue-deep:#0E4E96;
  --magenta:#DF0D83;
  --violet:#6A3E9A;
  --white:#ffffff;
  --ink:#111111;
  --muted:#8a8f99;
}
*{box-sizing:border-box;margin:0;padding:0}
html,body{width:1200px;height:538px;overflow:hidden;background:var(--white);font-family:"Inter",sans-serif}
.page{position:relative;width:1200px;height:538px}

.topbar{position:absolute;left:0;top:0;width:1200px;height:41px;
  background:linear-gradient(90deg,var(--blue) 0%,#3B4A9B 30%,var(--violet) 55%,#B12A8E 80%,var(--magenta) 100%);
  color:var(--white)}
.brand{position:absolute;left:112px;top:7px;line-height:1}
.brand-name{font-family:"Poppins",sans-serif;font-weight:600;font-size:18px;letter-spacing:.2px}
.brand-sub{display:block;text-align:right;font-size:6px;letter-spacing:.4px;margin-top:1px}
.divider{position:absolute;top:0;width:1px;height:41px;background:rgba(255,255,255,.35)}
.home{position:absolute;left:275px;top:12px;display:flex;align-items:center;gap:6px;font-size:14px}
.search{position:absolute;left:621px;top:6px;width:243px;height:28px;border-radius:14px;background:var(--white);
  display:flex;align-items:center;justify-content:space-between;padding:0 14px 0 16px;font-size:11.5px;color:var(--muted)}
.icon-mail{position:absolute;left:901px;top:13px}
.icon-bell{position:absolute;left:939px;top:9px}
.badge{position:absolute;left:10px;top:-1px;width:9px;height:9px;border-radius:50%;background:#F4E23A;color:#333;font-size:5px;text-align:center;line-height:9px}
.account{position:absolute;right:112px;top:7px;height:27px;display:flex;align-items:center;gap:8px}
.user{font-size:13px;white-space:nowrap}
.avatar{flex:none;width:27px;height:27px;border-radius:50%;
  background:radial-gradient(circle at 50% 45%,#D9A98A,#8C5A3E);border:1.5px solid rgba(255,255,255,.8)}

.apps{position:absolute;left:112px;top:90px;display:flex;gap:38px}
.app{position:relative;width:300px;text-align:center}
.app-photo{width:300px;height:263px;border-radius:32px 92px 45px 45px}
.photo-planning{background:linear-gradient(135deg,#5E86B8 0%,#2F5F93 45%,#1F3556 100%)}
.photo-tracking{background:linear-gradient(135deg,#E7D6CF 0%,#F4ECE8 45%,#C9A79A 80%,#6D4A3C 100%)}
.photo-performance{background:linear-gradient(160deg,#0B1630 0%,#102448 45%,#E0892A 75%,#2A8ED8 100%)}
.app-badge{position:absolute;left:113px;top:224px;width:74px;height:74px;border-radius:50%;
  background:linear-gradient(180deg,var(--magenta) 0%,#7A2C9C 55%,var(--blue-deep) 100%);
  display:flex;align-items:center;justify-content:center}
.app-title{margin-top:47px;font-family:"Poppins",sans-serif;font-weight:500;font-size:24px;color:var(--ink)}

.footer{position:absolute;left:0;top:486px;width:1200px;height:52px;background:var(--blue);color:var(--white)}
.copyright{position:absolute;left:112px;top:17px;font-size:13.5px}
.social{position:absolute;right:112px;top:12px;display:flex;gap:16px}
.social span{width:27px;height:27px;border:2px solid var(--white);border-radius:3px}
</style>
</head>
<body>
<div class="page">
  <header class="topbar">
    <div class="brand"><span class="brand-name">Tobin Quartz</span><span class="brand-sub">WEB APP PORTAL</span></div>
    <div class="divider" style="left:259px"></div>
    <div class="home">
      <svg width="16" height="15" viewBox="0 0 16 15" fill="none" stroke="#fff" stroke-width="1.8" stroke-linejoin="round"><path d="M1.5 7.5 8 1.5l6.5 6M3.5 6v7.5h3.5v-4h2v4h3.5V6"/></svg>
      <span>Home</span>
    </div>
    <div class="search"><span>Search Here</span>
      <svg width="14" height="14" viewBox="0 0 14 14" fill="none" stroke="#999" stroke-width="1.3"><circle cx="8" cy="6" r="4.5"/><path d="M4.8 9.2 1 13"/></svg>
    </div>
    <svg class="icon-mail" width="24" height="16" viewBox="0 0 24 16" fill="none" stroke="#fff" stroke-width="1.8"><rect x="1" y="1" width="22" height="14"/><path d="M1 1l11 8 11-8M1 15l8-7M23 15l-8-7"/></svg>
    <div class="icon-bell">
      <svg width="22" height="22" viewBox="0 0 22 22" fill="none" stroke="#fff" stroke-width="1.8"><path d="M5 15V10a6 6 0 0 1 12 0v5l2 2H3z"/><path d="M9 19a2 2 0 0 0 4 0"/></svg>
      <span class="badge">23</span>
    </div>
    <div class="divider" style="left:979px"></div>
    <div class="account">
      <span class="user">Ravi Dole</span>
      <div class="avatar" role="img" aria-label="User portrait"></div>
    </div>
  </header>

  <main class="apps">
    <section class="app">
      <div class="app-photo photo-planning" role="img" aria-label="Photo of hands typing on a laptop with scheduling icons"></div>
      <div class="app-badge">
        <svg width="40" height="40" viewBox="0 0 40 40" fill="none" stroke="#fff" stroke-width="2.2" stroke-linecap="round" stroke-linejoin="round">
          <rect x="6" y="6" width="22" height="28" rx="2"/><rect x="12" y="3" width="10" height="5" rx="1" fill="#fff"/>
          <path d="M9 14l2 2 3-3M9 21l2 2 3-3M9 28l2 2 3-3M17 15h8M17 22h6M17 29h3"/>
          <circle cx="29" cy="29" r="7" fill="#6A3E9A"/><path d="M29 25v4h3"/>
        </svg>
      </div>
      <h2 class="app-title">Jetty Planning</h2>
    </section>
    <section class="app">
      <div class="app-photo photo-tracking" role="img" aria-label="Photo of hands using a stylus on a tablet showing a map"></div>
      <div class="app-badge">
        <svg width="40" height="40" viewBox="0 0 40 40" fill="none" stroke="#fff" stroke-width="2" stroke-linejoin="round">
          <path d="M20 5l9 4.5v9L20 23l-9-4.5v-9z"/><path d="M11 9.5 20 14l9-4.5M20 14v9" />
          <circle cx="7" cy="32" r="2" fill="#fff"/><circle cx="33" cy="32" r="2" fill="#fff"/>
          <path d="M20 35c-3-3-3.5-4.5-3.5-6a3.5 3.5 0 0 1 7 0c0 1.5-.5 3-3.5 6z" fill="#fff"/>
          <path d="M11 32h3M26 32h3" />
        </svg>
      </div>
      <h2 class="app-title">Jetty Tracking</h2>
    </section>
    <section class="app">
      <div class="app-photo photo-performance" role="img" aria-label="Photo of an open hand beneath a glowing growth bar chart"></div>
      <div class="app-badge">
        <svg width="46" height="40" viewBox="0 0 46 40" fill="none" stroke="#fff" stroke-width="2.2" stroke-linecap="round" stroke-linejoin="round">
          <path d="M5 33h30"/><rect x="7" y="24" width="4" height="9" fill="#fff"/><rect x="14" y="20" width="4" height="13" fill="#fff"/><rect x="21" y="15" width="4" height="18" fill="#fff"/><rect x="28" y="10" width="4" height="23" fill="#fff"/>
          <path d="M5 20 24 8M19 7h6v6"/>
          <circle cx="38" cy="24" r="4"/><path d="M38 17v2M38 29v2M31 24h2M43 24h2M33 19l1.5 1.5M41.5 27.5 43 29M33 29l1.5-1.5M41.5 20.5 43 19"/>
        </svg>
      </div>
      <h2 class="app-title">Jetty/Port Performance</h2>
    </section>
  </main>

  <footer class="footer">
    <p class="copyright">© 2024 Tobin Quartz. All rights reserved.</p>
    <div class="social" aria-label="Social links"><span></span><span></span><span></span></div>
  </footer>
</div>
</body>
</html>
```